Ovaro Letterhead

Need a fresh looking design. We are a IT service company and I would like some elements of the logo to flow through. I have included the logo as an attachment. I have also included business card design as it might help with the design.

Industry/Entity Type

Business

```html
<!DOCTYPE html>
<html lang="en">
<head>
<meta charset="utf-8">
<title>Ovaro Letterhead</title>
<link rel="stylesheet" href="https://fonts.googleapis.com/css2?family=Questrial&display=swap">
<style>
  :root {
    --lime: #a4cd4a;
    --slate: #848d92;
    --slate-dark: #6f787d;
    --paper: #ffffff;
    --ink-light: #ffffff;
  }
  html, body {
    margin: 0;
    padding: 0;
    overflow: hidden;
    background: var(--paper);
  }
  .letterhead {
    position: relative;
    width: 927px;
    height: 1200px;
    overflow: hidden;
    background: var(--paper);
    font-family: "Questrial", sans-serif;
  }
  .header-art {
    position: absolute;
    left: 0;
    top: 0;
    width: 927px;
    height: 185px;
  }
  .brand-name {
    position: absolute;
    left: 40px;
    top: 38px;
    margin: 0;
    font-size: 66px;
    line-height: 1;
    font-weight: 400;
    letter-spacing: 1px;
    color: var(--ink-light);
  }
  .sender {
    position: absolute;
    left: 542px;
    top: 37px;
    color: var(--ink-light);
  }
  .sender-name {
    margin: 0;
    font-size: 11.5px;
    letter-spacing: 0.3px;
  }
  .sender-role {
    margin: 1px 0 5px;
    font-size: 8px;
    color: var(--lime);
  }
  .contact-list {
    list-style: none;
    margin: 0;
    padding: 0;
    font-size: 9.5px;
    color: var(--ink-light);
  }
  .contact-list li {
    display: flex;
    align-items: center;
    gap: 7px;
    height: 15px;
  }
  .contact-icon {
    width: 10px;
    height: 10px;
    flex: none;
  }
  .divider {
    position: absolute;
    left: 685px;
    top: 51px;
    width: 1px;
    height: 57px;
    background: var(--ink-light);
  }
  .office {
    position: absolute;
    left: 701px;
    top: 49px;
  }
  .footer-band {
    position: absolute;
    left: 0;
    bottom: 0;
    width: 927px;
    height: 53px;
    background: var(--slate);
  }
</style>
</head>
<body>
<div class="letterhead">
  <svg class="header-art" viewBox="0 0 1000 200" preserveAspectRatio="none" aria-hidden="true">
    <rect x="0" y="0" width="1000" height="134" fill="var(--lime)"/>
    <path d="M330 74 C 520 30, 760 16, 1000 28 L 1000 134 L 310 134 Z" fill="var(--slate)"/>
    <rect x="290" y="134" width="710" height="11" fill="var(--lime)"/>
    <path d="M0 138 C 40 176, 95 194, 165 194 C 245 194, 300 170, 324 134 L 300 120 Z" fill="var(--slate-dark)"/>
    <path d="M0 0 L 345 0 L 345 70 C 332 140, 265 186, 160 186 C 90 186, 35 166, 0 138 Z" fill="var(--lime)"/>
  </svg>

  <p class="brand-name">Ovaro</p>

  <div class="sender">
    <p class="sender-name">RK MADDEN</p>
    <p class="sender-role">I.T. Consultant</p>
    <ul class="contact-list">
      <li>
        <svg class="contact-icon" viewBox="0 0 10 10"><circle cx="5" cy="5" r="4.3" fill="none" stroke="var(--lime)" stroke-width="1"/><rect x="3.5" y="2.5" width="3" height="5" rx="0.6" fill="var(--lime)"/></svg>
        <span>0412 507 381</span>
      </li>
      <li>
        <svg class="contact-icon" viewBox="0 0 10 10"><circle cx="5" cy="5" r="4.3" fill="none" stroke="var(--lime)" stroke-width="1"/><rect x="2.6" y="3.3" width="4.8" height="3.4" fill="none" stroke="var(--lime)" stroke-width="0.8"/><path d="M2.6 3.3 L5 5.2 L7.4 3.3" fill="none" stroke="var(--lime)" stroke-width="0.8"/></svg>
        <span>rk@ovaro.com.au</span>
      </li>
    </ul>
  </div>

  <div class="divider"></div>

  <div class="office">
    <ul class="contact-list">
      <li>
        <svg class="contact-icon" viewBox="0 0 10 10"><circle cx="5" cy="5" r="4.3" fill="none" stroke="var(--lime)" stroke-width="1"/><path d="M5 2.4 C 3.6 2.4 3 3.4 3 4.2 C 3 5.4 5 7.6 5 7.6 C 5 7.6 7 5.4 7 4.2 C 7 3.4 6.4 2.4 5 2.4 Z" fill="var(--lime)"/></svg>
        <span>PO Box 2318, Larkfield 2041</span>
      </li>
      <li>
        <svg class="contact-icon" viewBox="0 0 10 10"><circle cx="5" cy="5" r="4.3" fill="none" stroke="var(--lime)" stroke-width="1"/><path d="M3.2 2.8 L4.3 2.6 L4.8 4 L4.1 4.6 C 4.5 5.4 5 5.9 5.7 6.2 L6.2 5.5 L7.5 6 L7.2 7.1 C 5 7.1 3.1 5 3.2 2.8 Z" fill="var(--lime)"/></svg>
        <span>02 9340 6612</span>
      </li>
      <li>
        <svg class="contact-icon" viewBox="0 0 10 10"><circle cx="5" cy="5" r="4.3" fill="var(--lime)"/><rect x="3" y="3.6" width="4" height="3" fill="var(--slate)"/></svg>
        <span>02 8571 2094</span>
      </li>
      <li>
        <svg class="contact-icon" viewBox="0 0 10 10"><circle cx="5" cy="5" r="4.3" fill="var(--lime)"/><circle cx="5" cy="5" r="2.2" fill="none" stroke="var(--slate)" stroke-width="0.8"/><path d="M2.8 5 H7.2 M5 2.8 V7.2" stroke="var(--slate)" stroke-width="0.6"/></svg>
        <span>www.ovaro.com.au</span>
      </li>
    </ul>
  </div>

  <div class="footer-band"></div>
</div>
</body>
</html>
```